Event Website for the Audio & Visual Industry

Convene is an exhibition aimed at meeting the business needs of audio and visual professionals – the visitors are the ones that make purchase decisions when buying anything to do with AV installation, Lighting & Entertainment Technology, DJ Technologies and even Musical Instruments.

We need to rebuild our website to reflect the professional look but with a bit of creativity/flare that is associated with the industry.

Websites whose design is along the lines we're looking for:

• http:www.marlowtech.com.au
• http:www.quenra.com
• http://www.brightpanelfair.example/ (competitor expo, like the layout. Not fantastic though, but the best I’ve seen from the industry)
• http://www.velmora.com.au and http://www.tralvick.com.au/ (Like these brand websites, they are clean and corporate but the use of imagery allows it to have some personality)

Target Market(s)

Corporate AV End Users, Lighting Designers, Concert/Entertainment companies, Sound Engineers

Industry/Entity Type

Business

Requirements
Must have
• Refer to the current splash page – www.convene-expo.example
This is the look and feel we have developed for our brochure. We want to expand on this and create a professional corporate look and feel without alienating existing sound, light and vision sectors.

The website's focus is to register visitors to attend the show. Please include a floating 'Register Free' Call to action. Please also include floating social media buttons. For what I mean by 'floating' check out the Social media buttons on this website: http://feedlorn.example/2012/02/19/glass-tower-trailer/ (scroll down to see effect).

We'll like to include a Rotating Banner at the top.

Sponsor element at the bottom off the page.

Sign up form functionality

Menu to be: About the Show, What's On, Register, How to Exhibit, Blog, Contact us.

I would like to see designs for a content page as well as the homepage.

```html
<!DOCTYPE html>
<html lang="en">
<head>
<meta charset="utf-8">
<title>Convene 2012 – Sound, Light, Vision</title>
<link href="https://fonts.googleapis.com/css2?family=Cabin:wght@400;500;700&family=Arimo:wght@400&family=Francois+One&display=swap" rel="stylesheet">
<style>
:root{
  --red:#c8161d;
  --red-dark:#9e0f14;
  --ink:#1c1c1c;
  --dark:#232323;
  --panel:#f3f3f3;
  --line:#cfcfcf;
  --muted:#555;
  --footer:#9b9b9b;
  --white:#fff;
}
*{margin:0;padding:0;box-sizing:border-box}
html,body{width:971px;height:1200px;overflow:hidden}
body{position:relative;background:#ececec;font-family:'Cabin',sans-serif;color:var(--ink)}
.abs{position:absolute}

.header{left:0;top:0;width:971px;height:144px;background:linear-gradient(180deg,#fdfdfd,#e9e9e9)}
.brand{left:78px;top:58px;display:flex;align-items:center;gap:10px}
.brand-mark{width:22px;height:22px;border-radius:50%;background:var(--red)}
.brand-name{font-size:42px;font-weight:500;color:var(--ink);letter-spacing:-0.5px}

.share{top:107px;display:flex;align-items:center;gap:4px}
.share-icon{width:21px;height:21px;border-radius:2px;background:#7a7a7a}
.share-count{height:14px;min-width:30px;padding:0 6px;border:1px solid #c5c5c5;border-radius:7px;background:#fff;font-size:8px;line-height:12px;text-align:center;color:#666}
.email-friend{left:838px;top:109px;display:flex;align-items:center;gap:7px;font-size:9px;color:#888}

.nav{left:0;top:144px;width:971px;height:31px;background:linear-gradient(180deg,#d8242a,#b3141a)}
.nav-tab{top:137px;left:46px;width:141px;height:38px;background:linear-gradient(180deg,#3a3a3a,#222);border-radius:4px 4px 0 0}
.nav-item{top:152px;font-family:'Arimo',sans-serif;font-size:13px;color:var(--white);transform:translateX(-50%);white-space:nowrap}

.stage{left:0;top:175px;width:971px;height:356px;background:repeating-linear-gradient(45deg,#262626 0 2px,#1e1e1e 2px 4px)}
.banner{left:49px;top:195px;width:888px;height:277px;background:linear-gradient(180deg,#c8321a 0%,#e05a22 40%,#b8401c 65%,#2a1b16 100%)}
.banner-caption{left:49px;top:371px;width:888px;height:76px;background:rgba(20,20,20,.55)}
.banner-text{left:66px;top:390px;font-size:15px;line-height:28px;font-weight:500;color:var(--white);letter-spacing:.3px}
.pager{left:408px;top:497px}
.register-cta{left:654px;top:484px;font-family:'Francois One',sans-serif;font-size:20px;color:#e0232a}
.signup-btn{left:803px;top:485px;width:115px;height:24px;border-radius:12px;background:linear-gradient(180deg,#fff,#d9d9d9);display:flex;align-items:center;font-size:12px;color:#222}
.signup-lock{width:20px;height:20px;border-radius:50%;background:var(--red);margin:0 14px 0 3px;display:flex;align-items:center;justify-content:center}

.intro{left:46px;top:565px;width:711px;height:107px;background:#e4e4e4}
.intro-title{left:66px;top:580px;font-size:12px;color:var(--red);letter-spacing:.2px}
.intro-copy{left:66px;top:602px;width:680px;font-size:11px;line-height:22px;color:#333}
.intro-video{left:764px;top:545px;width:149px;height:128px;background:linear-gradient(160deg,#8b8a80,#3b3a35 60%,#6b6355)}

.advances{left:46px;top:684px;width:879px;height:128px;background:repeating-linear-gradient(45deg,#232323 0 2px,#1b1b1b 2px 4px)}
.advances-title{left:77px;top:716px;font-size:21px;line-height:33px;color:#e0232a}
.adv-list{top:700px;list-style:none;font-size:13px;line-height:22px;color:var(--white)}
.adv-list li::before{content:"";display:inline-block;width:3px;height:3px;background:#fff;margin:0 10px 3px -13px}

.card{top:832px;width:279px;height:183px;background:var(--panel);border:1px solid var(--line);border-radius:6px}
.card-title{position:absolute;left:12px;top:15px;font-family:'Francois One',sans-serif;font-size:15px;color:#222;letter-spacing:.2px}
.card-photo{position:absolute;left:14px;top:42px;width:128px;height:107px}
.card-copy{position:absolute;left:155px;top:41px;width:120px;font-size:11px;line-height:22px;color:#333}
.card-more{position:absolute;left:196px;top:145px;font-size:11px;color:var(--red)}

.news-input{position:absolute;left:22px;top:44px;width:150px;height:29px;background:#7a7a7a;font-size:11px;color:#ddd;line-height:29px;padding-left:13px}
.news-submit{position:absolute;left:172px;top:44px;width:82px;height:29px;background:linear-gradient(180deg,#d8242a,#a9121a);font-size:11px;color:#fff;line-height:29px;text-align:center}
.connect{position:absolute;left:17px;top:103px;font-size:11px;color:#333}
.connect-icons{position:absolute;left:17px;top:137px;display:flex;gap:17px}
.connect-icons span{width:20px;height:20px;border-radius:2px;background:#7a7a7a}

.footer{left:0;top:1041px;width:971px;height:159px;background:linear-gradient(180deg,#a3a3a3,#949494)}
.footer-info{left:51px;top:1062px;font-family:'Arimo',sans-serif;font-size:11px;line-height:22.5px;color:#222}
.sponsors{left:406px;top:1067px;width:515px;height:59px;background:#b2b2b2;display:flex;align-items:center;justify-content:space-around;font-size:22px;color:#2a2a2a}
</style>
</head>
<body>

<header class="abs header"></header>
<div class="abs brand"><span class="brand-mark"></span><span class="brand-name">Convene</span></div>

<div class="abs share" style="left:497px"><span class="share-icon"></span><span class="share-count">55</span></div>
<div class="abs share" style="left:565px"><span class="share-icon"></span><span class="share-count">32</span></div>
<div class="abs share" style="left:635px"><span class="share-icon"></span><span class="share-count">25</span></div>
<div class="abs share" style="left:703px"><span class="share-icon"></span><span class="share-count">18</span></div>
<div class="abs share" style="left:772px"><span class="share-icon"></span></div>
<div class="abs email-friend">
  <svg width="23" height="16" viewBox="0 0 23 16"><rect x="0.5" y="0.5" width="22" height="15" fill="#f4f4f4" stroke="#aaa"/><path d="M1 1 L11.5 9 L22 1" fill="none" stroke="#aaa"/></svg>
  <span>Email to friend</span>
</div>

<nav>
  <div class="abs nav"></div>
  <div class="abs nav-tab"></div>
  <span class="abs nav-item" style="left:115px">About the Show</span>
  <span class="abs nav-item" style="left:265px">What's On</span>
  <span class="abs nav-item" style="left:403px">Register</span>
  <span class="abs nav-item" style="left:543px">How to Exhibit</span>
  <span class="abs nav-item" style="left:682px">Blog</span>
  <span class="abs nav-item" style="left:837px">Contact us</span>
</nav>

<section class="abs stage"></section>
<div class="abs banner" role="img" aria-label="Harbour opera house silhouetted against an orange sunset sky"></div>
<div class="abs banner-caption"></div>
<p class="abs banner-text">AUSTRALIA'S LARGEST AUDIO VISUALENTERTAINMENT &amp;INFORMATION<br>COMMUNICATIONS TECHNOLOGY EVENT</p>
<svg class="abs pager" width="195" height="34" viewBox="0 0 195 34">
  <path d="M0 34 C20 34 22 2 40 1 L155 1 C173 2 175 34 195 34 Z" fill="#3a3a3a"/>
  <circle cx="61" cy="17" r="5.5" fill="#eee"/>
  <circle cx="85" cy="17" r="5.5" fill="#111"/>
  <circle cx="109" cy="17" r="5.5" fill="#111"/>
  <circle cx="133" cy="17" r="5.5" fill="#111"/>
</svg>
<div class="abs register-cta">REGISTER FREE!</div>
<div class="abs signup-btn">
  <span class="signup-lock"><svg width="10" height="11" viewBox="0 0 10 11"><path d="M2.5 5 V3.5 a2.5 2.5 0 0 1 5 0 V5" fill="none" stroke="#fff" stroke-width="1.4"/><rect x="1" y="5" width="8" height="6" rx="1" fill="#fff"/></svg></span>
  Sign Up
</div>

<section>
  <div class="abs intro"></div>
  <h2 class="abs intro-title" style="font-weight:400">AUSTRALIA'S LARGEST AUDIO VISUALENTERTAINMENT &amp;INFORMATION&nbsp;&nbsp; COMMUNICATIONS TECHNOLOGY EVENT</h2>
  <p class="abs intro-copy">With over 500 brands on display, Convene in association with AVLink Global, brings together the worlds of ICT, integrating all areas including Visual, Education, Entertainment, Audio &amp;amp; Lighting Technology, Worship, Digital Signage and Unified Communications.</p>
  <div class="abs intro-video" role="img" aria-label="Video still of visitors walking the exhibition floor"></div>
</section>

<section>
  <div class="abs advances"></div>
  <h2 class="abs advances-title" style="font-weight:400">LATEST<br>ADVANCEMENTS</h2>
  <ul class="abs adv-list" style="left:296px"><li>Concert Production</li><li>AV Installation</li><li>Broadcast</li><li>Staging</li></ul>
  <ul class="abs adv-list" style="left:463px"><li>Lighting &amp; Entertainment&nbsp;&nbsp; Technology</li><li>Digital Media&nbsp;&nbsp; &amp;&nbsp;&nbsp; Information Services</li><li>Education Technology</li><li>Post Production</li></ul>
  <ul class="abs adv-list" style="left:723px"><li>Multimedia</li><li>Audio Engineering</li><li>Recording</li><li>DJ Technologies</li></ul>
</section>

<article class="abs card" style="left:45px">
  <h3 class="card-title" style="font-weight:400">CONTACT THE CONVENE TEAM</h3>
  <div class="card-photo" style="background:linear-gradient(150deg,#4a3a6a,#8a6fa8 45%,#2a2235)" role="img" aria-label="Sound engineers working at a mixing console"></div>
  <p class="card-copy">Lorem Ipsum is simply dummy text of the printing and typesetting industry.</p>
  <span class="card-more">View More</span>
</article>

<article class="abs card" style="left:347px">
  <h3 class="card-title" style="font-weight:400;left:27px">DOWNLOAD THE FLOOR PLAN</h3>
  <div class="card-photo" style="left:27px;background:linear-gradient(160deg,#8c8a80,#3a3935 60%,#6d6457)" role="img" aria-label="Video still of the busy exhibition floor"></div>
  <p class="card-copy" style="left:169px">Lorem Ipsum is simply dummy text of the printing and typesetting industry.</p>
  <span class="card-more" style="left:210px">View More</span>
</article>

<article class="abs card" style="left:650px">
  <h3 class="card-title" style="font-weight:400;left:21px">SIGN UP FOR NEWS LETTER</h3>
  <div class="news-input">Enter Your Email Id</div>
  <div class="news-submit">SUBMIT</div>
  <p class="connect">Connect With Us:</p>
  <div class="connect-icons"><span></span><span></span><span></span><span></span><span></span></div>
</article>

<footer>
  <div class="abs footer"></div>
  <p class="abs footer-info">© 2011 Harrowgate Exhibitions, Austrlia. All rights reserved.<br>Address&nbsp;&nbsp;&nbsp;&nbsp; : Level 2, 88 Kellaway Street,<br>&nbsp;&nbsp;&nbsp;&nbsp;&nbsp;&nbsp;&nbsp;&nbsp;&nbsp;&nbsp;&nbsp;&nbsp;&nbsp;&nbsp;&nbsp;&nbsp;&nbsp;&nbsp;&nbsp;&nbsp;Sydney, NSW 2000, Australia.<br>Telephone: +61 2 9000 4417<br>Facsimile:&nbsp;&nbsp; +61 2 9000 4418</p>
  <div class="abs sponsors"><span>Corvane</span><span>Tindle</span><span>Ostrava Soft</span><span>Kestrel Works</span></div>
</footer>

</body>
</html>
```